Joomla Responsive Website Template for an International Biotechnology Company

Our client is a biotechnology company that uses silver-based technology to help make products antimicrobial, antibacterial, and anti fungal. We need a Joomla-based template that is responsive/mobile friendly when viewed on tablets or smartphones. We are looking for a template design for the home page and subpages. We are replacing the current website http://www.velmora-labs.com with a new website being built here: http://velmoraclean.com.stagehost.com/velmoraprime/. What we have now on the site is the basic wire frame. This is the desired layout and pictures we want to use. We would like you to add some design elements to make the website more professional looking and polished. Please refer to the attached style guide to help you in choosing the color. The client does like the green leaf, which is included in the last page of style guide and may be good for a background image. While the Velmora logo and leaf are green, we do not want to overuse the color green. The client does own other technologies that we will be promoting on the site and the logos for these technologies are attached below. These logos are Tusk, Velmora-Prime, and Wisp. We will be using this website to promote the technologies, the markets the technologies serve; drinking water, medical devices, apparel and textiles, and architectural surfaces, and to promote the customer using these devices. Please make the design "clean" and not cluttered, as these technologies are used to fight "dirty things".
Updates

Hello Designers! Thank you all very much for your design submissions. They were simply excellent. Due to the Holidays and New Years, many of the client's team members have been on vacation. We expect to have feedback shortly and pick the top design soon there after. Again, thank you all very much and hope the New Year brings you continued success. Best, Dorian

Industry/Entity Type

Biotechnology

Coding

Coded - Design and coding required

```html
<!DOCTYPE html>
<html lang="en">
<head>
<meta charset="utf-8">
<title>Velmora Antimicrobial</title>
<link rel="stylesheet" href="https://fonts.googleapis.com/css2?family=Questrial&family=Arimo:wght@400;700&display=swap">
<style>
:root{
  --green:#77c043;
  --green-dark:#5fa62f;
  --green-light:#c8ef8a;
  --ink:#222;
  --text:#333;
  --grey-bg:#efefef;
  --footer:#3a3d42;
  --footer-text:#9a9da2;
  --white:#fff;
}
*{box-sizing:border-box;margin:0;padding:0}
html,body{width:1200px;height:2404px;overflow:hidden;background:var(--white)}
body{position:relative;font-family:"Arimo",Arial,sans-serif;color:var(--text)}
.abs{position:absolute}

/* header */
.site-header{position:absolute;left:0;top:0;width:1200px;height:82px;background:var(--white);z-index:3}
.brand-name{position:absolute;left:58px;top:0;height:82px;line-height:78px;font-family:"Arimo",sans-serif;font-weight:700;font-size:44px;color:var(--green);letter-spacing:-1px}
.main-nav{position:absolute;top:0;left:0;height:82px;font-size:13px;text-transform:uppercase;color:var(--ink)}
.main-nav span{position:absolute;top:0;height:82px;line-height:70px;white-space:nowrap}
.main-nav .active{background:var(--green);color:var(--white);padding:0 17px;font-weight:700}

/* hero */
.hero{position:absolute;left:0;top:82px;width:1200px;height:690px;background:radial-gradient(ellipse at 62% 48%,#f4f5f6 0%,#dfe2e5 45%,#b9c0c8 75%,#e9ebed 100%)}
.hero-title{position:absolute;left:70px;top:212px;font-family:"Questrial",sans-serif;font-weight:400;font-size:70px;line-height:80px;color:#111;letter-spacing:2px}
.slider-bar{position:absolute;left:0;top:772px;width:1200px;height:38px;background:var(--green)}
.slider-dots{position:absolute;left:600px;top:780px;display:flex;gap:5px}
.slider-dots i{width:14px;height:14px;border-radius:50%;border:2px solid var(--white);background:var(--white)}
.slider-dots i.off{background:transparent}

/* about */
.about{position:absolute;left:0;top:810px;width:1200px;height:412px;background:linear-gradient(#ededed,#f8f8f8)}
.leaf{position:absolute;left:0;top:10px;width:680px;height:400px;background:radial-gradient(ellipse at 30% 45%,#a6d85c 0%,#7fbf35 45%,#5a9a1e 75%,rgba(248,248,248,0) 100%);border-radius:0 60% 0 0}
.section-title{position:absolute;left:0;width:1200px;text-align:center;font-family:"Questrial",sans-serif;font-size:40px;color:var(--ink)}
.title-rule{position:absolute;left:420px;width:360px;height:2px;background:linear-gradient(90deg,transparent,#bbb,transparent)}
.about-copy{position:absolute;left:678px;top:136px;width:484px;font-size:14.5px;line-height:24px;color:var(--text)}
.read-more{position:absolute;left:1012px;top:372px;font-size:15px;color:var(--ink);display:flex;align-items:center;gap:10px}
.circle-arrow{width:22px;height:22px;border-radius:50%;background:var(--green);display:inline-flex;align-items:center;justify-content:center}

/* markets */
.markets{position:absolute;left:0;top:1222px;width:1200px;height:498px;background:linear-gradient(#8fcf4e 0%,#7bc142 45%,#6ab332 100%)}
.market{position:absolute;top:134px;width:230px;text-align:center;color:var(--white)}
.market-icon{width:128px;height:110px;margin:0 auto;border:2px solid rgba(255,255,255,.35);border-radius:16px;background:rgba(255,255,255,.12);display:flex;align-items:center;justify-content:center}
.market-icon.first{background:rgba(255,255,255,.35)}
.market h3{margin-top:18px;font-size:22px;line-height:27px;font-weight:700;text-transform:uppercase;letter-spacing:.5px}
.market p{margin-top:10px;font-size:13.5px;line-height:19px;color:var(--green-light);height:38px;overflow:hidden}
.market p.light{color:var(--white)}
.market .more{width:22px;height:22px;margin:22px auto 0;border:2px solid var(--white);border-radius:50%;display:flex;align-items:center;justify-content:center}

/* customers */
.customers{position:absolute;left:0;top:1720px;width:1200px;height:150px;background:var(--white)}
.customer{position:absolute;top:60px;height:36px;display:flex;align-items:center;justify-content:center;font-family:"Arimo",sans-serif;font-weight:700;font-size:24px;color:#1d2a5a}

/* news */
.news{position:absolute;left:0;top:1870px;width:1200px;height:350px;background:var(--grey-bg)}
.news-card{position:absolute;top:130px;width:238px;height:170px;background:var(--white);border-radius:10px;box-shadow:3px 4px 0 var(--green-dark)}
.news-date{height:52px;background:linear-gradient(#8fd050,#71b93a);border-radius:10px 10px 0 0;color:var(--white);font-family:"Questrial",sans-serif;font-size:21px;line-height:52px;padding-left:14px}
.news-card p{padding:14px 12px 0 18px;font-size:12.5px;line-height:16px;color:var(--ink)}
.news-card .circle-arrow{position:absolute;right:14px;bottom:10px;width:20px;height:20px}
.chev{position:absolute;top:2070px;width:18px;height:18px;border-radius:50%;background:var(--white);display:flex;align-items:center;justify-content:center}

/* footer */
.site-footer{position:absolute;left:0;top:2220px;width:1200px;height:184px;background:var(--footer);color:var(--footer-text)}
.footer-brand{position:absolute;left:66px;top:40px;height:80px;line-height:80px;font-weight:700;font-size:46px;color:var(--white);letter-spacing:-1px}
.copyright{position:absolute;left:66px;top:136px;font-size:13px;color:var(--white)}
.footer-divider{position:absolute;left:350px;top:44px;height:104px;border-left:2px dashed var(--white)}
.footer-label{font-size:19px;font-weight:700;color:var(--white)}
.footer-text{font-size:14px;line-height:22px;color:var(--footer-text)}
.social{display:flex;gap:18px;margin-top:22px;font-size:14px;font-weight:700;color:var(--white)}
</style>
</head>
<body>

<header class="site-header">
  <div class="brand-name">Velmora</div>
  <nav class="main-nav">
    <span class="active" style="left:294px">Home</span>
    <span style="left:394px">About Us</span>
    <span style="left:492px">Markets</span>
    <span style="left:588px">Technology</span>
    <span style="left:708px">Customer</span>
    <span style="left:814px">Programs</span>
    <span style="left:922px">News</span>
    <span style="left:996px">Highlights</span>
    <span style="left:1104px">Contact Us</span>
  </nav>
</header>

<section class="hero" role="img" aria-label="Close-up photograph of a chrome stethoscope with blue tubing on a white background">
  <h1 class="hero-title">HIGH QUALITY<br>MEDICAL DEVICES</h1>
</section>
<div class="slider-bar"></div>
<div class="slider-dots"><i></i><i class="off"></i><i></i></div>

<section class="about">
  <div class="leaf" role="img" aria-label="Macro photograph of a bright green leaf with its veins"></div>
  <h2 class="section-title" style="top:20px">Velmora® Antimicrobial</h2>
  <div class="title-rule" style="top:86px"></div>
  <p class="about-copy">Velmora branded antimicrobial technology makes products cleaner and longer lasting with silver, copper and zinc, which have been proven in use throughout history. Velmora antimicrobial technology provides built-in protection by working 24/7 resisting the growth of microbes. We work in close partnership with our customers, from development to end-user marketing, to deliver a product advantage that makes a real difference in the marketplace.<br>*Velmora is an EPA registered ionic silver technology and is not a nanosilver technology.</p>
  <div class="read-more">Read more <span class="circle-arrow"><svg width="10" height="10" viewBox="0 0 10 10"><path d="M3 1l4 4-4 4" stroke="#fff" stroke-width="2" fill="none"/></svg></span></div>
</section>

<section class="markets">
  <div class="market" style="left:117px">
    <div class="market-icon first"><svg width="36" height="50" viewBox="0 0 36 50"><path d="M18 2C12 16 4 24 4 34a14 14 0 0 0 28 0C32 24 24 16 18 2z" fill="#fff"/></svg></div>
    <h3>Drinking<br>Water</h3>
    <p class="light">Clean and Efficient Water purity and quality have far reaching</p>
    <div class="more"><svg width="8" height="8" viewBox="0 0 10 10"><path d="M3 1l4 4-4 4" stroke="#fff" stroke-width="2" fill="none"/></svg></div>
  </div>
  <div class="market" style="left:370px">
    <div class="market-icon"><svg width="60" height="56" viewBox="0 0 60 56" fill="none" stroke="#fff" stroke-width="4" stroke-linecap="round"><path d="M8 4v16a12 12 0 0 0 24 0V4"/><path d="M20 32v8a10 10 0 0 0 20 0v-6"/><circle cx="40" cy="28" r="6"/></svg></div>
    <h3>Medical<br>Devices</h3>
    <p>positive displacement Needle Connector with Velmora's Antimi-</p>
    <div class="more"><svg width="8" height="8" viewBox="0 0 10 10"><path d="M3 1l4 4-4 4" stroke="#fff" stroke-width="2" fill="none"/></svg></div>
  </div>
  <div class="market" style="left:623px">
    <div class="market-icon"><svg width="60" height="52" viewBox="0 0 60 52" fill="none" stroke="#fff" stroke-width="4" stroke-linejoin="round"><path d="M20 4l-16 10 6 10 6-4v28h28V20l6 4 6-10-16-10c-2 6-6 8-10 8s-8-2-10-8z"/></svg></div>
    <h3>Apparel &amp;<br>Textiles</h3>
    <p>Military footwear/Tactical boots, Activewear textiles, footwear</p>
    <div class="more"><svg width="8" height="8" viewBox="0 0 10 10"><path d="M3 1l4 4-4 4" stroke="#fff" stroke-width="2" fill="none"/></svg></div>
  </div>
  <div class="market" style="left:880px">
    <div class="market-icon"><svg width="56" height="52" viewBox="0 0 56 52" fill="#fff"><path d="M28 2L4 14v4h48v-4z"/><rect x="8" y="22" width="6" height="20"/><rect x="20" y="22" width="6" height="20"/><rect x="31" y="22" width="6" height="20"/><rect x="42" y="22" width="6" height="20"/><rect x="4" y="44" width="48" height="5"/></svg></div>
    <h3>Architectural<br>Surfaces</h3>
    <p>The Global leader in door opening solutions, PVC free and commer</p>
    <div class="more"><svg width="8" height="8" viewBox="0 0 10 10"><path d="M3 1l4 4-4 4" stroke="#fff" stroke-width="2" fill="none"/></svg></div>
  </div>
</section>

<section class="customers">
  <div class="customer" style="left:140px;width:120px">Brellan</div>
  <div class="customer" style="left:360px;width:140px;font-size:20px">Castorel</div>
  <div class="customer" style="left:556px;width:140px;font-size:20px">Clearwell</div>
  <div class="customer" style="left:776px;width:116px;font-size:22px;color:#111">Mondri</div>
  <div class="customer" style="left:976px;width:130px;color:#2a5fa8">Aquilo</div>
</section>

<section class="news">
  <h2 class="section-title" style="top:42px">News &amp; Events</h2>
  <div class="title-rule" style="top:104px"></div>
  <article class="news-card" style="left:58px"><div class="news-date">DEC 10, 2014</div><p>New Society of Clinical Hygiene Practice (SCHP) Guidelines Include Velmora Antimicrobial-Treated Catheters</p><span class="circle-arrow"><svg width="8" height="8" viewBox="0 0 10 10"><path d="M3 1l4 4-4 4" stroke="#fff" stroke-width="2" fill="none"/></svg></span></article>
  <article class="news-card" style="left:330px"><div class="news-date">DEC 10, 2014</div><p>Harbor City Marathon Winner Wears Strydon Shoes Protected by Velmora Antimicrobial</p><span class="circle-arrow"><svg width="8" height="8" viewBox="0 0 10 10"><path d="M3 1l4 4-4 4" stroke="#fff" stroke-width="2" fill="none"/></svg></span></article>
  <article class="news-card" style="left:606px"><div class="news-date">DEC 10, 2014</div><p>Norvance Strengthens and Expands Technical Sales and Services Efforts with New Hire in West Asia(2)</p><span class="circle-arrow"><svg width="8" height="8" viewBox="0 0 10 10"><path d="M3 1l4 4-4 4" stroke="#fff" stroke-width="2" fill="none"/></svg></span></article>
  <article class="news-card" style="left:884px"><div class="news-date">DEC 10, 2014</div><p>New Society of Clinical Hygiene Practice (SCHP) Guidelines Include Velmora Antimicrobial-Treated Catheters</p><span class="circle-arrow"><svg width="8" height="8" viewBox="0 0 10 10"><path d="M3 1l4 4-4 4" stroke="#fff" stroke-width="2" fill="none"/></svg></span></article>
</section>
<span class="chev" style="left:20px"><svg width="8" height="8" viewBox="0 0 10 10"><path d="M7 1L3 5l4 4" stroke="#555" stroke-width="2" fill="none"/></svg></span>
<span class="chev" style="left:1144px"><svg width="8" height="8" viewBox="0 0 10 10"><path d="M3 1l4 4-4 4" stroke="#555" stroke-width="2" fill="none"/></svg></span>

<footer class="site-footer">
  <div class="footer-brand">Velmora</div>
  <div class="copyright">©&nbsp; 2014 | Privacypolicy</div>
  <div class="footer-divider"></div>
  <div class="abs" style="left:448px;top:48px">
    <div class="footer-label">Address</div>
    <div class="footer-text" style="margin-top:8px">24 Larkspur Road<br>Fairhaven, MA 02719</div>
  </div>
  <div class="abs" style="left:708px;top:56px;display:flex;align-items:center;gap:12px">
    <svg width="20" height="20" viewBox="0 0 24 24" fill="#9a9da2"><path d="M6.6 10.8a15 15 0 0 0 6.6 6.6l2.2-2.2c.3-.3.7-.4 1-.2 1.1.4 2.3.6 3.6.6.6 0 1 .4 1 1V20c0 .6-.4 1-1 1A17 17 0 0 1 3 4c0-.6.4-1 1-1h3.5c.6 0 1 .4 1 1 0 1.3.2 2.5.6 3.6.1.3 0 .7-.2 1z"/></svg>
    <span style="font-size:17px;font-weight:700;color:#fff">555-014-7101</span>
  </div>
  <div class="abs" style="left:708px;top:96px;display:flex;align-items:center;gap:12px">
    <svg width="20" height="20" viewBox="0 0 24 24" fill="none" stroke="#9a9da2" stroke-width="1.8"><circle cx="12" cy="12" r="10"/><ellipse cx="12" cy="12" rx="4" ry="10"/><path d="M2 12h20"/></svg>
    <span class="footer-text" style="font-size:15px">www.norvance.com</span>
  </div>
  <div class="abs" style="left:1000px;top:54px">
    <div class="footer-label">follow us</div>
    <div class="social"><span>Linkora</span><span>Chirpo</span></div>
  </div>
</footer>

</body>
</html>
```